Clean, creative business Wordpress Site

Our company is building a website via Wordpress and needs a clean, no fuss, modern looking design that reflects our company brand (see attached logos).

In addition, the company is a woman owned business (no middle-aged white guy stock photos please) and primarily works with the oil & gas industry. We would prefer no images with direct references to energy (rigs, windmills, solar panels, etc.). Part of our consulting is providing thought leadership around energy politics and policy so creative ways to incorporate that visually will be appreciated as well.

Site map of pages below:

Home
- About
- Team
- Expertise
- Blog

We prefer a header image that includes the company logo and easy to identify and navigate menus.

Target Market(s)

Energy professionals, Executives

Industry/Entity Type

Consulting

Font styles to use
Serif

Colors
85acd3
0255a3
cedeed
ffffff

Requirements
Must have
• Clean and easy to navigate, clear menus, simple design that reflects company logo.

```html
<!DOCTYPE html>
<html lang="en">
<head>
<meta charset="utf-8">
<title>Corvanta Energy</title>
<link rel="stylesheet" href="https://fonts.googleapis.com/css2?family=Lora:wght@400;700&family=Roboto:wght@400;500;700&display=swap">
<style>
:root{
  --blue:#0255a3;
  --sky:#85acd3;
  --mist:#cedeed;
  --white:#ffffff;
  --grey-band:#e9e9e9;
  --ink:#3a3a3a;
  --navy:#0d2650;
  --rule:#d6d6d6;
}
*{box-sizing:border-box;margin:0;padding:0}
html,body{width:1200px;height:2542px;overflow:hidden;background:var(--white)}
body{position:relative;font-family:"Roboto",Arial,sans-serif;color:var(--ink)}
.abs{position:absolute}
.serif{font-family:"Lora",Georgia,serif}

/* header */
.site-header{left:0;top:0;width:1200px;height:85px;background:var(--white)}
.brand{left:76px;top:22px;display:flex;align-items:center;gap:12px}
.brand-mark{width:30px;height:30px;background:var(--blue)}
.brand-name{font-family:"Lora",Georgia,serif;font-size:30px;color:var(--blue);font-weight:400;letter-spacing:.5px}
.main-nav{right:72px;top:29px;display:flex;gap:8px}
.main-nav a{display:block;padding:0 11px;height:30px;line-height:30px;font-size:16px;font-weight:500;color:#333;text-decoration:none}
.main-nav a.is-active{background:var(--blue);color:var(--white)}

/* hero */
.hero{left:0;top:85px;width:1200px;height:492px;background:linear-gradient(135deg,#3c4048 0%,#8c8a86 40%,#c9c4bb 60%,#4a4440 100%)}

/* welcome */
.welcome-title{left:75px;top:636px;font-size:22px;font-weight:400;color:#333;letter-spacing:.5px}
.welcome-title b{color:var(--blue);font-weight:700}
.welcome-text{left:75px;top:682px;width:696px;font-size:13.5px;line-height:22.5px;color:#444}
.btn{display:inline-block;background:var(--sky);color:var(--white);font-size:13px;text-transform:uppercase;padding:0 10px;height:25px;line-height:25px}
.welcome-btn{left:75px;top:822px}
.welcome-photo{left:793px;top:641px;width:334px;height:207px;background:linear-gradient(120deg,#2f3338,#6b6f72 50%,#3b3a36)}

/* blog */
.blog-band{left:0;top:915px;width:1200px;height:48px;background:var(--blue)}
.band-title{left:75px;top:925px;font-family:"Lora",Georgia,serif;font-weight:700;font-size:21px;color:var(--white)}
.band-btn{left:1042px;top:927px}
.blog-area{left:0;top:963px;width:1200px;height:244px;background:var(--grey-band)}
.post{width:322px;top:996px}
.post-date{font-size:12.5px;color:#333}
.post-title{margin-top:15px;font-size:13.5px;line-height:22px;color:var(--blue)}
.post-body{margin-top:10px;font-size:13.5px;line-height:22px;color:#444}
.post-more{margin-top:10px;font-size:13px;color:var(--sky)}

/* expertise */
.expertise{left:0;top:1207px;width:1200px;height:698px;background:linear-gradient(180deg,#2c73ae,#1f66a3)}
.exp-title{left:453px;top:1272px;width:294px;height:44px;border:1.5px solid var(--white);color:var(--white);font-family:"Lora",Georgia,serif;font-size:30px;font-weight:400;line-height:41px;text-align:center}
.exp-title b{font-weight:700}
.exp-rule{top:1293px;height:1.5px;background:var(--white);width:72px}
.exp-label{color:var(--white);font-size:22px;font-weight:700;white-space:nowrap}
.exp-btn{left:558px;top:1815px;background:var(--mist);color:var(--blue)}

/* team */
.team-title{left:75px;top:1963px;font-size:22px;font-weight:400;color:#333}
.team-title b{color:var(--blue);font-weight:700}
.team-btn{left:1042px;top:1965px}
.team-rule{left:75px;top:1998px;width:1050px;height:1px;background:var(--rule)}
.team-divider{left:599px;top:2010px;width:1px;height:180px;background:var(--rule)}
.portrait{width:153px;height:167px;top:2022px;background:linear-gradient(180deg,#cfd3d6,#8f969c)}
.member{top:2020px;width:330px}
.member-name{font-size:16px;font-weight:700;color:var(--blue)}
.member-role{font-size:13.5px;color:#444;margin-top:3px}
.member-bio{margin-top:14px;font-size:13.5px;line-height:22px;color:#444}

/* footer (children positioned relative to footer) */
.site-footer{left:0;top:2254px;width:1200px;height:288px;background:var(--blue)}
.talk{left:183px;top:46px;font-size:35px;line-height:38px;color:var(--white);font-weight:400}
.talk span{color:var(--sky);display:block}
.contact-label{font-size:12px;color:var(--mist);text-transform:uppercase}
.contact-value{font-size:19px;line-height:24px;color:var(--white)}
.msg-btn{left:811px;top:105px;width:122px;height:32px;border-radius:16px;background:var(--navy);color:var(--white);font-size:14px;font-weight:700;text-align:center;line-height:32px}
.social{top:161px;width:32px;height:32px;border:2px solid var(--white);border-radius:50%}
.copyright{left:0;top:240px;width:1200px;text-align:center;color:var(--white);font-size:14px}
</style>
</head>
<body>

<header class="site-header abs">
  <div class="brand abs"><span class="brand-mark"></span><span class="brand-name">Corvanta Energy</span></div>
  <nav class="main-nav abs">
    <a class="is-active" href="#">HOME</a><a href="#">ABOUT</a><a href="#">TEAM</a><a href="#">EXPERTISE</a><a href="#">BLOG</a>
  </nav>
</header>

<div class="hero abs" role="img" aria-label="Diverse team of colleagues laughing together around a meeting table"></div>

<section>
  <h1 class="welcome-title abs serif">WELCOME TO <b>CORVANTA ENERGY</b></h1>
  <p class="welcome-text abs">Lorem ipsum dolor sit amet, consectetur adipiscing elit, sed do eiusmod tempor incididunt ut labore et dolore magna aliqua. Ut enim ad minim veniam, quis nostrud exercitation ullamco laboris nisi ut aliquip ex ea commodo consequat. Duis aute irure dolor in reprehenderit in voluptate velit esse cillum dolore eu fugiat nulla pariatur. Excepteur sint occaecat cupidatat non proident, sunt in culpa qui officia deserunt mollit anim id est laborum.</p>
  <span class="welcome-btn btn abs">Learn more</span>
  <div class="welcome-photo abs" role="img" aria-label="Two professionals meeting at a laptop in an office"></div>
</section>

<section>
  <div class="blog-band abs"></div>
  <h2 class="band-title abs">LATEST BLOG</h2>
  <span class="band-btn btn abs">View all</span>
  <div class="blog-area abs"></div>
  <article class="post abs" style="left:75px">
    <div class="post-date">NOV 17, 2016</div>
    <div class="post-title">Lorem ipsum dolor sit amet, consectetur adipiscing elit</div>
    <div class="post-body">sed do eiusmod tempor incididunt ut labore et dolore magna aliqua. Ut enim ad minim veniam, quis nostrud exercitation.</div>
    <div class="post-more">Read More&rsaquo;</div>
  </article>
  <article class="post abs" style="left:434px">
    <div class="post-date">NOV 17, 2016</div>
    <div class="post-title">Lorem ipsum dolor sit amet, consectetur adipiscing elit</div>
    <div class="post-body">sed do eiusmod tempor incididunt ut labore et dolore magna aliqua. Ut enim ad minim veniam, quis nostrud exercitation.</div>
    <div class="post-more">Read More&rsaquo;</div>
  </article>
  <article class="post abs" style="left:793px">
    <div class="post-date">NOV 17, 2016</div>
    <div class="post-title">Lorem ipsum dolor sit amet, consectetur adipiscing elit</div>
    <div class="post-body">sed do eiusmod tempor incididunt ut labore et dolore magna aliqua. Ut enim ad minim veniam, quis nostrud exercitation.</div>
    <div class="post-more">Read More&rsaquo;</div>
  </article>
</section>

<section>
  <div class="expertise abs" role="img" aria-label="Blue-tinted photo of a meeting room with people at a table"></div>
  <div class="exp-rule abs" style="left:381px"></div>
  <div class="exp-rule abs" style="left:747px"></div>
  <h2 class="exp-title abs">OUR <b>EXPERTISE</b></h2>

  <svg class="abs" style="left:0;top:1207px" width="1200" height="698" viewBox="0 1207 1200 698" fill="none" stroke="#fff" stroke-width="2">
    <polygon points="600,1361 739,1500 600,1639 461,1500" fill="#fff" stroke="none"/>
    <polygon points="390,1449 441,1500 390,1551 339,1500"/>
    <polygon points="807,1449 858,1500 807,1551 756,1500"/>
    <polygon points="487,1559 538,1610 487,1661 436,1610"/>
    <polygon points="712,1559 763,1610 712,1661 661,1610"/>
    <polygon points="600,1657 651,1708 600,1759 549,1708"/>
    <g fill="#fff" stroke="none">
      <circle cx="382" cy="1493" r="5"/><circle cx="398" cy="1493" r="5"/><circle cx="390" cy="1489" r="6"/>
      <path d="M374 1512 q8-14 16 0 q8-14 16 0 z"/><path d="M380 1512 q10-18 20 0 z"/>
    </g>
    <path d="M793 1486 l9 9 m0-7 v7 h-7 M821 1486 l-9 9 m0-7 v7 h7 M793 1514 l9-9 m0 7 v-7 h-7 M821 1514 l-9-9 m0 7 v-7 h7"/>
    <path d="M477 1594 h14 l7 7 v25 h-21 z M481 1606 h13 M481 1612 h13 M481 1618 h9"/>
    <circle cx="712" cy="1604" r="9"/><path d="M707 1614 v6 h10 v-6 M708 1624 h8"/>
    <path d="M586 1724 h28 M589 1722 v-8 M596 1722 v-12 M603 1722 v-16 M610 1722 v-22" stroke-width="4"/>
  </svg>
  <div class="exp-label abs" style="left:100px;top:1518px">Community Engagement</div>
  <div class="exp-label abs" style="left:846px;top:1518px">Deescalating Conflict</div>
  <div class="exp-label abs" style="left:272px;top:1629px">Navigating Policy</div>
  <div class="exp-label abs" style="left:750px;top:1629px">Energy Access</div>
  <div class="exp-label abs" style="left:506px;top:1766px">Investor Relations</div>
  <span class="exp-btn btn abs">View all</span>
</section>

<section>
  <h2 class="team-title abs serif">OUR <b>TEAM</b></h2>
  <span class="team-btn btn abs">View all</span>
  <div class="team-rule abs"></div>
  <div class="team-divider abs"></div>
  <div class="portrait abs" style="left:75px" role="img" aria-label="Portrait of team member Dana Whitfield"></div>
  <div class="member abs" style="left:252px">
    <div class="member-name">DANA WHITFIELD</div>
    <div class="member-role">Lorem ipsum</div>
    <p class="member-bio">Sed ut perspiciatis unde omnis iste natus error sit voluptatem accusantium doloremque laudantium, totam rem aperiam, eaque ipsa quae ab illo inventore veritatis et quasi architecto beatae vitae dicta sunt explicabo.</p>
  </div>
  <div class="portrait abs" style="left:613px" role="img" aria-label="Portrait of team member Marcus Hale"></div>
  <div class="member abs" style="left:793px">
    <div class="member-name">MARCUS HALE</div>
    <div class="member-role">Lorem ipsum</div>
    <p class="member-bio">Sed ut perspiciatis unde omnis iste natus error sit voluptatem accusantium doloremque laudantium, totam rem aperiam, eaque ipsa quae ab illo inventore veritatis et quasi architecto beatae vitae dicta sunt explicabo.</p>
  </div>
</section>

<footer class="site-footer abs">
  <div class="talk abs">Let's talk.<span>We love</span><span>to listen.</span></div>

  <svg class="abs" style="left:420px;top:52px" width="40" height="40" viewBox="0 0 40 40" fill="none" stroke="#fff" stroke-width="2">
    <path d="M8 10 q2-6 8-6 l4 8 -4 4 q4 8 12 12 l4-4 8 4 q0 6-6 8 q-22-4-26-26z"/>
  </svg>
  <div class="abs" style="left:475px;top:51px">
    <div class="contact-label">Call</div><div class="contact-value">123-456-5555</div>
  </div>

  <svg class="abs" style="left:422px;top:114px" width="40" height="44" viewBox="0 0 40 44" fill="none" stroke="#fff" stroke-width="2">
    <path d="M20 4 c-8 0-12 6-12 12 0 8 12 22 12 22 s12-14 12-22 c0-6-4-12-12-12z"/><circle cx="20" cy="16" r="4"/>
  </svg>
  <div class="abs" style="left:475px;top:116px">
    <div class="contact-label">Visit</div>
    <div class="contact-value">Your Company LTD.<br>Street Name, 000000<br>City Name</div>
  </div>

  <svg class="abs" style="left:758px;top:44px" width="40" height="40" viewBox="0 0 40 40" fill="none" stroke="#fff" stroke-width="2">
    <path d="M6 30 l3-9 17-17 6 6 -17 17 z M23 7 l6 6"/>
  </svg>
  <div class="abs" style="left:800px;top:46px;width:1px;height:52px;background:var(--white)"></div>
  <div class="abs" style="left:811px;top:51px">
    <div class="contact-label">Write</div><div class="contact-value">info@corvantaenergy.com</div>
  </div>
  <div class="msg-btn abs">MESSAGE US</div>
  <span class="social abs" style="left:810px"></span>
  <span class="social abs" style="left:848px"></span>

  <div class="copyright abs">© 2017 Corvanta Energy. All rights reserved.</div>
</footer>

</body>
</html>
```